Business Card Design for company

We want new business cards. We'd like something different-- yet still highly professional. Our tagline is Guiding Projects, Building Results. Stock photos are ok, as long as they are relevant and look upscale.

Target Market(s)

Architecture/Business Management Consulting/Engineering Consulting

Contact Information for Business Card

dark gray background with pops of blue might be good, but you tell me. You're the designers. Rounded corners might be nice, but again, you tell me.

Font styles to use
Serif
Sans Serif

Colors
3276b5
5c5c5c
9d9d9d
fbfbfb

Requirements
Nice to have
• Something different, but still very professional.

```html
<!DOCTYPE html>
<html lang="en">
<head>
<meta charset="utf-8">
<title>Norvale Advisory – Business Card</title>
<link href="https://fonts.googleapis.com/css2?family=Work+Sans:wght@400;500;600&display=swap" rel="stylesheet">
<style>
  :root {
    --stage: #1c1c1d;
    --card: #262627;
    --card-back: #1f1f20;
    --blue: #3276b5;
    --grey-dark: #5c5c5c;
    --grey: #9d9d9d;
    --white: #fbfbfb;
  }
  * { margin: 0; padding: 0; box-sizing: border-box; }
  html, body {
    width: 1200px; height: 900px; overflow: hidden;
    background: radial-gradient(ellipse at 50% 40%, #2c2c2d 0%, var(--stage) 75%);
    font-family: "Work Sans", Arial, sans-serif;
  }
  .card {
    position: absolute;
    left: 250px;
    width: 700px;
    height: 400px;
    border-radius: 4px;
    box-shadow: 0 14px 30px rgba(0,0,0,.55);
    overflow: hidden;
  }
  .card--back { top: 36px; background: var(--card-back); }
  .card--front { top: 464px; background: var(--card); }

  .back-texture {
    position: absolute; inset: 0;
    background: linear-gradient(110deg, #1d1d1e 0%, #2a2a2b 55%, #3a3a3b 100%);
  }
  .back-name {
    position: absolute; left: 0; right: 0; top: 50%;
    transform: translateY(-50%);
    width: 260px; margin: 0 auto;
    padding: 6px 0;
    text-align: center;
    font-size: 46px; font-weight: 600; letter-spacing: 2px;
    color: var(--blue);
    background: var(--card-back);
  }

  .front-heading {
    position: absolute; top: 30px; left: 0; right: 0;
    text-align: center;
    font-size: 14px; letter-spacing: 1px;
    color: var(--grey-dark);
  }
  .brand {
    position: absolute; left: 56px; top: 108px; width: 300px;
    color: var(--blue);
    font-weight: 600;
    line-height: 1;
  }
  .brand__main { display: block; font-size: 60px; letter-spacing: 1px; }
  .brand__sub { display: block; font-size: 28px; letter-spacing: 9px; margin-top: 12px; }
  .divider {
    position: absolute; left: 372px; top: 98px;
    width: 2px; height: 186px; background: var(--white);
  }
  .contact { position: absolute; left: 400px; top: 104px; color: var(--white); }
  .contact__name {
    font-size: 27px; font-weight: 500; letter-spacing: 2px;
    color: var(--blue); text-transform: uppercase;
  }
  .contact__role { font-size: 16px; margin: 2px 0 14px; }
  .contact__address { font-size: 16px; line-height: 1.35; margin-bottom: 10px; }
  .contact__line {
    display: flex; align-items: center; gap: 9px;
    font-size: 16px; line-height: 1.55;
  }
  .contact__line svg { width: 12px; height: 12px; flex: none; }
  .tagline {
    position: absolute; left: 0; right: 0; bottom: 34px;
    text-align: center;
    font-size: 19px; font-weight: 500; letter-spacing: .5px;
    color: var(--white);
  }
</style>
</head>
<body>

<section class="card card--back">
  <div class="back-texture" role="img" aria-label="Tonal embossed pattern of the company name repeated across the card"></div>
  <div class="back-name">Norvale</div>
</section>

<section class="card card--front">
  <p class="front-heading">Dependable Project Delivery Partner for Over Two Decades.</p>

  <div class="brand">
    <span class="brand__main">NORVALE</span>
    <span class="brand__sub">ADVISORY</span>
  </div>

  <div class="divider"></div>

  <div class="contact">
    <h1 class="contact__name">Daniel Hart</h1>
    <p class="contact__role">Director</p>
    <p class="contact__address">112b Harbour Lane,<br>Westbridge, NZ, 4020</p>
    <p class="contact__line">
      <svg viewBox="0 0 12 12" aria-hidden="true"><path d="M2.5 1l2 2.3-1 1.3c.7 1.4 1.7 2.4 3 3l1.3-1L10 8.6 9 10.8C5 10.5 1.5 7 1.2 2.8z" fill="#3276b5"/></svg>
      (555) 214-7730
    </p>
    <p class="contact__line">
      <svg viewBox="0 0 12 12" aria-hidden="true"><rect x="1" y="2.5" width="10" height="7" fill="none" stroke="#3276b5" stroke-width="1"/><path d="M1 2.5l5 4 5-4" fill="none" stroke="#3276b5" stroke-width="1"/></svg>
      info@norvaleadvisory.com
    </p>
    <p class="contact__line">
      <svg viewBox="0 0 12 12" aria-hidden="true"><circle cx="6" cy="6" r="5" fill="none" stroke="#3276b5"/><ellipse cx="6" cy="6" rx="2.2" ry="5" fill="none" stroke="#3276b5"/><path d="M1 6h10" stroke="#3276b5"/></svg>
      www.norvaleadvisory.com
    </p>
  </div>

  <p class="tagline">Guiding Projects, Building Results</p>
</section>

</body>
</html>
```